Fenmoor Business Card

I want a business card for me and my employees.
On one side it must be in Greek and on the other side in English. The color must much the one of the logo

Target Market(s)

Customers that are looking for security and antipiracy advisors

Contact Information for Business Card

Title, Email, Phone, website , Mobile Address Zip code, city and country

Requirements
Must have
• The colors of our logo (the blue ones)

```html
<!DOCTYPE html>
<html lang="en">
<head>
<meta charset="utf-8">
<title>Fenmoor Advisory — Business Cards</title>
<link href="https://fonts.googleapis.com/css2?family=Roboto:wght@400;700&display=swap" rel="stylesheet">
<style>
  :root {
    --page-bg: #efefef;
    --card-bg: #fafafa;
    --navy: #27225c;
    --text-grey: #5f5f66;
    --band-grey: #b3b4b3;
    --white: #ffffff;
  }
  * { box-sizing: border-box; margin: 0; padding: 0; }
  html, body {
    width: 1200px; height: 1052px; overflow: hidden;
    background: var(--page-bg);
    font-family: "Roboto", Arial, sans-serif;
  }
  .canvas { position: relative; width: 1200px; height: 1052px; }
  .card {
    position: absolute; left: 324px; width: 552px; height: 334px;
    background: var(--card-bg); overflow: hidden;
  }
  .card--greek { top: 172px; }
  .card--english { top: 546px; }

  .brand { position: absolute; left: 24px; top: 37px; display: flex; align-items: center; gap: 10px; }
  .brand__mark { width: 56px; height: 75px; background: var(--navy); }
  .brand__name {
    color: var(--navy); font-weight: 700; font-size: 34px; line-height: 36px;
    letter-spacing: 1px; text-transform: uppercase;
  }

  .person { position: absolute; left: 24px; top: 186px; }
  .person__name { color: var(--navy); font-weight: 700; font-size: 20px; line-height: 24px; }
  .person__title { color: var(--text-grey); font-size: 14px; line-height: 18px; margin-top: 1px; }

  .address {
    position: absolute; left: 24px; top: 259px;
    color: var(--text-grey); font-size: 14px; line-height: 21px;
  }

  .contacts { position: absolute; left: 333px; top: 203px; list-style: none; }
  .contacts li {
    display: flex; align-items: center; height: 21px;
    color: var(--text-grey); font-size: 14px;
  }
  .contacts svg { width: 16px; height: 14px; margin-right: 13px; fill: var(--navy); }

  .footer { position: absolute; left: 0; top: 0; width: 552px; height: 334px; }
  .footer__company {
    position: absolute; left: 335px; top: 301px;
    color: var(--white); font-size: 14px; line-height: 20px;
  }
</style>
</head>
<body>
<main class="canvas">

  <section class="card card--greek" lang="el">
    <svg class="footer" viewBox="0 0 552 334" aria-hidden="true">
      <rect x="0" y="320" width="290" height="14" fill="var(--band-grey)"/>
      <path d="M276 334 L298 300 Q304 291 316 291 L552 291 L552 334 Z" fill="var(--navy)"/>
    </svg>
    <div class="brand">
      <div class="brand__mark"></div>
      <div class="brand__name">Fenmoor<br>Advisory</div>
    </div>
    <div class="person">
      <h2 class="person__name">Τζον Ντόε Σμιθ</h2>
      <p class="person__title">Διευθύνων Σύμβουλος</p>
    </div>
    <p class="address">234 Οπουδήποτε St., οποιαδήποτε πόλη,<br>Οποιαδήποτε πόλη, ΗΠΑ 123456</p>
    <ul class="contacts">
      <li><svg viewBox="0 0 16 14"><path d="M1 5 Q8 -1 15 5 L12 6 L11 4 H5 L4 6 Z M4 7 H12 L14 13 H2 Z"/></svg>828-111-1111</li>
      <li><svg viewBox="0 0 16 14"><rect x="1" y="2" width="14" height="10"/></svg>Τζον@yourwebsite.com</li>
      <li><svg viewBox="0 0 16 14"><circle cx="8" cy="7" r="6"/></svg>www.yourwebsite.com</li>
    </ul>
    <p class="footer__company">Fenmoor Advisory LTP</p>
  </section>

  <section class="card card--english">
    <svg class="footer" viewBox="0 0 552 334" aria-hidden="true">
      <rect x="0" y="320" width="290" height="14" fill="var(--band-grey)"/>
      <path d="M276 334 L298 300 Q304 291 316 291 L552 291 L552 334 Z" fill="var(--navy)"/>
    </svg>
    <div class="brand">
      <div class="brand__mark"></div>
      <div class="brand__name">Fenmoor<br>Advisory</div>
    </div>
    <div class="person">
      <h2 class="person__name">John Doe Smith</h2>
      <p class="person__title">Managing Director</p>
    </div>
    <p class="address">234 Anywhere St., Any City,<br>Any Town, US 123456</p>
    <ul class="contacts">
      <li><svg viewBox="0 0 16 14"><path d="M1 5 Q8 -1 15 5 L12 6 L11 4 H5 L4 6 Z M4 7 H12 L14 13 H2 Z"/></svg>828-111-1111</li>
      <li><svg viewBox="0 0 16 14"><rect x="1" y="2" width="14" height="10"/></svg>john@yourwebsite.com</li>
      <li><svg viewBox="0 0 16 14"><circle cx="8" cy="7" r="6"/></svg>www.yourwebsite.com</li>
    </ul>
    <p class="footer__company">Fenmoor Advisory LTP</p>
  </section>

</main>
</body>
</html>
```